Business Card for Coach - ready to print

Design Business Card ready to order prints www.lukasbrenner.coach

* An Overview / Background of the Business & Services
· Coaching
· Personal growth
* The Target Market / Audience you are trying to reach
· private person in different roles (self, familiy, business role)s
* Design Specifics; any preferences or ideas for Style, Colour, Imagery, etc
· See www.lukasbrenner.coach
· "simple" design
· (small) element of surprise / unusual element

* Information that will be placed in the Business Card
· Beratung und Coaching
· Address: Lukas Brenner, Talmatt 42, CH-8531 Winterthur, Mobile +41 76 254 63 07
* Do you have an existing website or Facebook page where designers can learn more about your company?
· lukasbrenner.coach

Target Market(s)

private person in different roles (self, familiy, business role)

Industry/Entity Type

Life Coaching

Contact Information for Business Card

Lukas Brenner
Talmatt 42
CH-8531 Winterthur

Mobile: +41 76 254 63 07
Email: lubr@sonnwelt.ch
www.lukasbrenner.coach

Font styles to use
Sans Serif

Colors

Designer to choose colors to be used in the design.

Requirements
Must have
• "simple" design
• element of surprise / unusual element
• Beratung & Coaching
• see www.lukasbrenner.coach for colors and so...
Nice to have
• TA Symbol (three rings on top of each other) - unsual presentation
• QR Code of Website (see if it fits in and still looks good).

```html
<!DOCTYPE html>
<html lang="de">
<head>
<meta charset="utf-8">
<title>Lukas Brenner – Visitenkarte</title>
<link rel="stylesheet" href="https://fonts.googleapis.com/css2?family=Oswald:wght@500&family=Arimo:wght@400&display=swap">
<style>
  :root{
    --brand-red:#a21f24;
    --ink:#4a4a4a;
    --ink-soft:#5c5c5c;
    --name-grey-light:#c4c4c4;
    --paper:#ffffff;
    --backdrop:#e9e9eb;
  }
  html,body{margin:0;padding:0;width:1200px;height:800px;overflow:hidden;background:var(--backdrop);}
  .sheet{position:relative;width:1200px;height:800px;display:flex;align-items:center;justify-content:center;gap:48px;}
  .card{position:relative;width:540px;height:340px;overflow:hidden;box-shadow:0 6px 18px rgba(0,0,0,.18);}
  .name{position:absolute;font-family:"Oswald",sans-serif;font-weight:500;font-size:31px;line-height:1;letter-spacing:-.5px;white-space:nowrap;transform:scaleX(.86);}
  .name .first{margin-right:5px;}

  /* front side */
  .card--front{background:var(--brand-red);}
  .front-bar{position:absolute;left:0;top:276px;width:336px;height:20px;background:var(--paper);}
  .card--front .name{right:18px;top:262px;transform-origin:right center;}
  .card--front .first{color:var(--name-grey-light);}
  .card--front .last{color:var(--paper);}
  .tagline{position:absolute;right:20px;top:306px;margin:0;font-family:"Arimo",sans-serif;font-size:12px;letter-spacing:.4px;color:var(--paper);}

  /* back side */
  .card--back{background:var(--paper);}
  .back-stripe{position:absolute;left:258px;right:0;top:205px;height:16px;background:var(--brand-red);}
  .card--back .name{left:22px;top:190px;transform-origin:left center;}
  .card--back .first{color:var(--ink-soft);}
  .card--back .last{color:var(--brand-red);}
  .contact-list{position:absolute;left:24px;top:238px;margin:0;padding:0;list-style:none;font-family:"Arimo",sans-serif;font-size:14px;color:var(--ink);}
  .contact-list li{display:flex;align-items:center;gap:9px;height:23px;}
  .contact-list svg{width:12px;height:12px;flex:none;}
  .accent{color:var(--brand-red);}
  .address{position:absolute;right:26px;top:236px;margin:0;font-family:"Arimo",sans-serif;font-style:normal;font-size:14px;line-height:21px;color:var(--ink);text-align:right;}
</style>
</head>
<body>
<main class="sheet">

  <section class="card card--front" aria-label="Vorderseite">
    <div class="front-bar"></div>
    <div class="name"><span class="first">LUKAS</span><span class="last">BRENNER</span></div>
    <p class="tagline">Beratung &amp; Coaching</p>
  </section>

  <section class="card card--back" aria-label="Rückseite">
    <div class="back-stripe"></div>
    <div class="name"><span class="first">LUKAS</span><span class="last">BRENNER</span></div>
    <ul class="contact-list">
      <li>
        <svg viewBox="0 0 12 12" aria-hidden="true"><rect x="1.5" y="1.5" width="9" height="9" fill="none" stroke="var(--brand-red)" stroke-width="1.6"/></svg>
        <span>+41 76 254 63 07</span>
      </li>
      <li>
        <svg viewBox="0 0 12 12" aria-hidden="true"><rect x="0.5" y="2" width="11" height="8" fill="var(--brand-red)"/><path d="M0.5 2 L6 6.5 L11.5 2" fill="none" stroke="#fff" stroke-width="1"/></svg>
        <span>lubr@sonnwelt.ch</span>
      </li>
      <li>
        <svg viewBox="0 0 12 12" aria-hidden="true"><circle cx="6" cy="6" r="5.5" fill="var(--brand-red)"/><path d="M0.5 6 H11.5 M6 0.5 V11.5 M6 0.5 C3 3 3 9 6 11.5 M6 0.5 C9 3 9 9 6 11.5" fill="none" stroke="#fff" stroke-width=".7"/></svg>
        <span>www.<span class="accent">lukasbrenner</span>.coach</span>
      </li>
    </ul>
    <address class="address">Talmatt 42<br>CH-8531 Winterthur</address>
  </section>

</main>
</body>
</html>
```